New Packaging Design Project

Wine packaging redesign. Retail partner requested a redesign of a private label wine. The old label is attached. Our partner liked the Lantern and Briar label and wanted something similar. There will be a logo added to the top of the label

Went on vacation/holiday

```html
<!DOCTYPE html>
<html lang="en">
<head>
<meta charset="UTF-8">
<title>Napa Valley Red Blend 2018 Label</title>
<link rel="stylesheet" href="https://fonts.googleapis.com/css2?family=Marcellus&family=Jost:wght@400;500&display=swap">
<style>
  :root {
    --page: #f4f4f2;
    --label-light: #82817e;
    --label-mid: #767572;
    --label-dark: #5c5c5a;
    --gold: #e2aa4c;
    --ink-light: #f2f2f0;
    --hills-dark: #2f302f;
    --hills-mid: #3b3d3a;
    --vine-green: #5f6f3a;
    --mountain: #4b4c4c;
  }
  * { margin: 0; padding: 0; box-sizing: border-box; }
  html, body {
    width: 1200px;
    height: 2400px;
    overflow: hidden;
    background: var(--page);
  }
  .canvas {
    position: relative;
    width: 1200px;
    height: 2400px;
  }
  .wine-label {
    position: absolute;
    left: 60px;
    top: 384px;
    width: 1080px;
    height: 1632px;
    background: radial-gradient(ellipse at 50% 30%, var(--label-light) 0%, var(--label-mid) 55%, var(--label-dark) 100%);
    overflow: hidden;
  }
  .appellation {
    position: absolute;
    top: 532px;
    left: 0;
    width: 100%;
    text-align: center;
    font-family: "Marcellus", serif;
    font-size: 102px;
    line-height: 1;
    letter-spacing: 1px;
    color: var(--gold);
  }
  .title-rule {
    position: absolute;
    top: 643px;
    left: 50%;
    width: 158px;
    height: 4px;
    margin-left: -79px;
    background: var(--gold);
  }
  .wine-style {
    position: absolute;
    top: 664px;
    left: 0;
    width: 100%;
    text-align: center;
    font-family: "Jost", sans-serif;
    font-weight: 500;
    font-size: 52px;
    line-height: 1;
    letter-spacing: 5px;
    color: var(--gold);
  }
  .varietals {
    position: absolute;
    top: 750px;
    left: 0;
    width: 100%;
    text-align: center;
    font-family: "Jost", sans-serif;
    font-weight: 400;
    font-size: 30px;
    line-height: 43px;
    letter-spacing: 0.5px;
    color: var(--ink-light);
  }
  .varietals .divider {
    display: inline-block;
    margin: 0 12px;
  }
  .vintage {
    position: absolute;
    top: 852px;
    left: 0;
    width: 100%;
    text-align: center;
    font-family: "Jost", sans-serif;
    font-weight: 500;
    font-size: 42px;
    line-height: 1;
    color: var(--ink-light);
  }
  .vineyard-scene {
    position: absolute;
    left: 0;
    top: 900px;
    width: 100%;
    height: 732px;
    background:
      linear-gradient(180deg,
        rgba(0,0,0,0) 0%,
        var(--mountain) 9%,
        var(--hills-mid) 24%,
        var(--vine-green) 46%,
        var(--hills-dark) 66%,
        var(--vine-green) 84%,
        var(--hills-dark) 100%);
  }
</style>
</head>
<body>
  <main class="canvas">
    <section class="wine-label">
      <h1 class="appellation">NAPA VALLEY</h1>
      <div class="title-rule"></div>
      <h2 class="wine-style">RED BLEND</h2>
      <p class="varietals">
        MERLOT<span class="divider">|</span>CABARNET SAUVIGNON<br>
        CABERNET FRANC<span class="divider">|</span>PETIT VERDOT<span class="divider">|</span>MALBEC
      </p>
      <p class="vintage">2018</p>
      <div class="vineyard-scene" role="img" aria-label="Illustration of distant mountains above rolling striped vineyard hills in dark grey and olive green"></div>
    </section>
  </main>
</body>
</html>
```